QPM Habitat Helpers 2019

We need a 2 page flyer to advertise our upcoming program. The program covers 5 months May-September 2019 and is focused on conservation.I have attached some options that i like. It needs to be striking.

Text in newly uploaded document 'HHFlyer2'

Target Market(s)

Conservation
Conscious travelers
30-45 year olds
Environmental
Adventure/Hiking
Citizen Science

Font styles to use
Sans Serif

Colors
0355a3
fbed22

Requirements
Must have
• A travel conservation focus
• Highlight the significance of the 'in the world' status of the project
Nice to have
• A yellow border, making it look similar to the cover of Wandering Horizons

```html
<!DOCTYPE html>
<html lang="en">
<head>
<meta charset="utf-8">
<title>QPM Habitat Helpers 2019 – Flyer</title>
<link href="https://fonts.googleapis.com/css2?family=Bebas+Neue&family=Oswald:wght@600;700&family=Source+Sans+3:wght@400;600;700&display=swap" rel="stylesheet">
<style>
:root{
  --navy:#1f3a8a;
  --blue:#0355a3;
  --sky:#0aa0e0;
  --yellow:#fbed22;
  --ink:#4a4a4a;
  --paper:#ffffff;
  --bg:#e4e4e2;
}
*{box-sizing:border-box;margin:0;padding:0}
html,body{width:1200px;height:837px;overflow:hidden;background:var(--bg)}
body{position:relative;font-family:"Source Sans 3",Arial,sans-serif}
.page{position:absolute;top:44px;width:521px;height:735px;background:var(--paper);overflow:hidden;box-shadow:0 4px 14px rgba(0,0,0,.25)}
.page--left{left:51px}
.page--right{left:631px}

.photo{position:absolute;left:0;top:0;width:100%}
.photo--coast{height:370px;clip-path:polygon(0 0,100% 0,100% 290px,0 366px);background:linear-gradient(160deg,#2f7a3a 0%,#4f8f43 16%,#1b6fa0 38%,#1597b8 58%,#2aa7b5 78%,#7cb9c4 100%)}
.photo--lookout{height:360px;background:linear-gradient(180deg,#3d86c8 0%,#8fc0e6 30%,#dbe8f0 48%,#8fa4b4 58%,#5b7f58 75%,#3d5a2f 100%)}

.banner{position:absolute;height:46px;background:var(--yellow);color:var(--navy);font-family:"Oswald",sans-serif;font-weight:700;font-size:34px;line-height:46px;letter-spacing:-.5px;white-space:nowrap}
.banner__url{position:absolute;top:46px;height:26px;background:var(--navy);color:#fff;font-family:"Source Sans 3",sans-serif;font-weight:700;font-size:17px;line-height:26px;letter-spacing:0;padding:0 12px;white-space:nowrap}
.page--left .banner{left:-10px;top:80px;width:560px;padding-left:28px;transform:rotate(-8deg);transform-origin:left top}
.page--left .banner__url{left:0;width:250px;text-align:left}
.page--right .banner{left:132px;top:-6px;width:430px;padding-left:14px;transform:rotate(10deg);transform-origin:left top}
.page--right .banner__url{right:30px;width:260px;text-align:right}

.headline{position:absolute;left:28px;top:155px;color:#fff;font-family:"Bebas Neue",sans-serif;font-weight:400;font-size:25px;line-height:27px}
.intro{position:absolute;left:28px;top:243px;width:285px;color:#fff;font-weight:600;font-size:12.5px;line-height:14px}

.panel{position:absolute;background:linear-gradient(180deg,var(--sky) 0%,#1a7fcc 40%,var(--blue) 75%,var(--navy) 100%);color:#fff}
.page--left .panel{left:322px;top:218px;width:199px;height:517px;clip-path:polygon(0 84px,100% 0,100% 100%,0 100%)}
.page--right .panel{left:0;top:218px;width:162px;height:517px;clip-path:polygon(0 0,100% 48px,100% 100%,0 100%)}

.badge{position:absolute;width:126px;height:126px;border-radius:50%;background:#fff;border:5px solid var(--blue);display:flex;align-items:center;justify-content:center;text-align:center;color:var(--blue);font-weight:700;font-size:15px;line-height:17px}
.page--left .badge{left:361px;top:215px}
.page--right .badge{left:18px;top:216px}
.badge::before{content:"";position:absolute;inset:6px;border-radius:50%;border:2px solid var(--blue)}

.quote{position:absolute;left:332px;top:364px;width:182px;font-size:11.5px;line-height:15px;font-weight:600;color:#fff}
.quote__mark{font-family:"Oswald",sans-serif;font-size:24px;line-height:10px;vertical-align:-6px;margin-right:4px}
.quote cite{display:block;font-style:normal;font-weight:400;font-size:9.5px;line-height:14px}
.panel-copy{position:absolute;left:332px;top:430px;width:180px;color:#fff}
.panel-copy p{font-size:9.6px;line-height:12.2px;text-align:justify;margin-bottom:12px}
.panel-footer{position:absolute;top:698px;text-align:center;color:var(--yellow);font-size:11.5px;line-height:14px}
.page--left .panel-footer{left:322px;width:199px}
.page--right .panel-footer{left:0;width:162px}

.events{list-style:none}
.event__photo{position:absolute;left:22px;width:67px;height:67px;border-radius:50%;border:2px solid #fff;box-shadow:0 0 0 1px #ccc}
.event__body{position:absolute;left:99px;width:214px}
.event__title{font-family:"Bebas Neue",sans-serif;font-weight:400;font-size:10.5px;line-height:11px;color:var(--navy);white-space:nowrap}
.event__text{font-size:8px;line-height:8.7px;color:var(--ink);text-align:justify}

.pillars{list-style:none;color:#fff;font-weight:600;font-size:17px;line-height:17px}
.pillars li{position:absolute;left:22px;white-space:nowrap}
.pillars b{color:var(--yellow);font-size:22px;font-weight:700}
.panel-rule{position:absolute;left:8px;top:672px;width:148px;border-top:1px solid rgba(255,255,255,.8)}

.seal{position:absolute;left:426px;top:244px;width:66px;height:66px;border-radius:50%;background:radial-gradient(circle,#f3d27a 0%,#d9a92c 70%,#b8861c 100%)}

.facts{position:absolute;left:169px;top:362px;width:334px}
.facts p{font-size:10px;line-height:12.2px;color:var(--ink);text-align:justify;margin-bottom:10px}
.facts p.facts__small{font-size:9px;line-height:11px}
.facts-rule{position:absolute;left:169px;top:672px;width:334px;border-top:1px solid var(--navy)}

.partners{position:absolute;left:172px;top:692px;width:334px;height:26px;display:flex;align-items:center;gap:9px}
.partner{background:#c9ced6;flex:none}
.partner--round{width:24px;height:18px;border-radius:50%}
.partner--sq{width:18px;height:18px}
.partner--wide{width:42px;height:14px}
.partner-name{margin-left:auto;color:var(--blue);font-weight:700;font-size:9px;line-height:11px}
</style>
</head>
<body>

<section class="page page--left">
  <div class="photo photo--coast" role="img" aria-label="Aerial view of a turquoise lagoon, reef and green headland"></div>

  <div class="banner">MAKE A DIFFERENCE IN 2019
    <span class="banner__url">www.qpmhabitat.info</span>
  </div>

  <h1 class="headline">THE BEST WAY TO EXPERIENCE<br>THE TRUE BEAUTY OF QUILL POINT ISLAND<br>IS TO SEE IT FOR YOURSELF;</h1>
  <p class="intro">Join our QPM HABITAT HELPERS program in 2019 and be involved in a world class, award winning holistic conservation Effort – protecting paradise.</p>

  <div class="panel"></div>
  <div class="badge">QPM Habitat<br>Helpers</div>

  <blockquote class="quote"><span class="quote__mark">“</span>Quill Point Island is]so extra-ordinary it is almost unbelievable”.<cite>- Sir Douglas Ashcombe</cite></blockquote>
  <div class="panel-copy">
    <p>Quill Point Island located 600km off the New South Wales coast is renowned for its spectacular scenery, important breeding grounds for colonies of seabirds, and its rich biodiversity including many endangered and critically endangered species not found anywhere else in the world.</p>
    <p>QPM Habitat Helpers believe in protecting Quill Point Island's unique biodiversity while showcasing world class conservation in action.</p>
    <p>We are dedicated to empowering like-minded people to make a difference through robust citizen science, inspiring educational experiences, and tangible local conservation action.</p>
  </div>
  <p class="panel-footer">For more details, visit<br>www.qpmhabitat.info</p>

  <ul class="events">
    <li class="event">
      <div class="event__photo" role="img" aria-label="Seabird chick resting on the ground" style="top:357px;background:linear-gradient(135deg,#8a8f88,#4e5a4c)"></div>
      <div class="event__body" style="top:364px">
        <h3 class="event__title">Birds of Quill Point Island – May 2019</h3>
        <p class="event__text">Showcasing Quill Point Island's incredible bird species. Experience the amazing phenomena of 'calling' wild seabirds down from the sky as you assist in research into the life of rare seabirds.</p>
      </div>
    </li>
    <li class="event">
      <div class="event__photo" role="img" aria-label="Snorkeller surveying the reef underwater" style="top:429px;background:linear-gradient(135deg,#2a8fc6,#0d4e7e)"></div>
      <div class="event__body" style="top:434px">
        <h3 class="event__title">Quill Point Island's Marine Environment – June 2019</h3>
        <p class="event__text">Our seabirds are being impacted by ocean plastic debris. Help survey Quill Point Island's diverse intertidal ecosystems and provide valuable data to help understand the issue and support solutions.</p>
      </div>
    </li>
    <li class="event">
      <div class="event__photo" role="img" aria-label="Forested mountain peaks" style="top:502px;background:linear-gradient(160deg,#9fb7c6,#4d6b3b 55%,#2f4a26)"></div>
      <div class="event__body" style="top:504px">
        <h3 class="event__title">Invasive Species – July 2019</h3>
        <p class="event__text">Invasive weeds are identified as one of the most serious threats to Quill Point Island's biodiversity and world heritage values. Hike to remote and settlement locations and assist in weed removal with our experts, whilst learning about our world class Weed Eradication Program.</p>
      </div>
    </li>
    <li class="event">
      <div class="event__photo" role="img" aria-label="Volunteers gathered around a field survey table" style="top:573px;background:linear-gradient(135deg,#7a8a5c,#3f4d33)"></div>
      <div class="event__body" style="top:574px">
        <h3 class="event__title">Amazing Invertebrates – August 2019</h3>
        <p class="event__text">Rodents are voracious predators of invertebrates. The loss of invertebrates is particularly significant because invertebrates play an important role in maintaining natural ecological functions. This month we will celebrate the discovery and revival of the rare Phasmid and the wider context of invertebrate conservation on Quill Point Island and across the globe.</p>
      </div>
    </li>
    <li class="event">
      <div class="event__photo" role="img" aria-label="Young visitor enjoying the island outdoors" style="top:649px;background:linear-gradient(135deg,#5fb7c9,#2d8aa3)"></div>
      <div class="event__body" style="top:654px">
        <h3 class="event__title">Protecting Paradise – September 2019</h3>
        <p class="event__text">September will showcase the very best of our island conservation. Quill Point Island has a long history of sustainability and conservation programs ensuring the Island's unique biodiversity is safeguarded. Recently winning the prestigious national gold Wattle award as well as the sustainability award for government, adding to 2 Blue Planet awards and a TERRA award in 2018.</p>
      </div>
    </li>
  </ul>
</section>

<section class="page page--right">
  <div class="photo photo--lookout" role="img" aria-label="Hiker standing on a ridge overlooking the island lagoon and distant peaks"></div>

  <div class="banner">MAKE A DIFFERENCE IN 2019
    <span class="banner__url">www.qpmhabitat.info</span>
  </div>

  <div class="seal" role="img" aria-label="Award seal"></div>

  <div class="panel"></div>
  <div class="badge">QPM Habitat<br>Helpers</div>

  <ul class="pillars">
    <li style="top:421px">Wo<b>R</b>ld Heritage</li>
    <li style="top:460px">Conservati<b>O</b>n<br>Volunteers</li>
    <li style="top:503px">Adven<b>T</b>ure</li>
    <li style="top:541px">Citiz<b>E</b>n Science</li>
    <li style="top:584px">World<b>C</b>lass</li>
    <li style="top:630px">Relaxa<b>T</b>ion</li>
  </ul>
  <div class="panel-rule"></div>
  <p class="panel-footer">For more details, visit<br>www.qpmhabitat.info</p>

  <div class="facts">
    <p>Quill Point Island is considered to be an outstanding example of an island ecosystem developed from submarine volcanic activity. One of the last settled islands in the world, Quill Point Island's almost untouched environment needs to be protected.</p>
    <p>In 1982, The Quill Point Island Group was listed as a Global Heritage Council World Heritage property, in recognition of the global significance of the island's beauty and biodiversity.</p>
    <p>Connect with nature through conservation and contribute to data collection used to aid research on environmental issues.</p>
    <p>The perfect place for true adventure, unexplored environments, undiscovered species, all level hiking, unique activities and amazing views.</p>
    <p class="facts__small">Citizen science is reconnecting people with wildlife and the environment helping science and conservation and sparking imaginations and passions in the process.</p>
    <p>Quill Point Island's renowned pristine natural environment is maintained through world-class conservation efforts that began more than 100 years ago and continue today.</p>
    <p>Breathtaking scenery, pristine environment, no mobile reception. The perfect place to take some time out and relax.</p>
  </div>
  <div class="facts-rule"></div>

  <div class="partners">
    <span class="partner partner--round"></span>
    <span class="partner partner--sq"></span>
    <span class="partner partner--sq"></span>
    <span class="partner partner--wide"></span>
    <span class="partner partner--sq"></span>
    <span class="partner partner--sq"></span>
    <span class="partner partner--wide"></span>
    <span class="partner-name">QUILL POINT ISLAND</span>
  </div>
</section>

</body>
</html>
```